Corporate Power Point Template

Tarrowmead Group, Inc. produces and sells ready-mixed concrete, aggregates, and concrete-related products and services for the construction industry in the United States.

We are looking for a simple and sleek design that will look great on a projector, as well as when printed on paper. We prefer a lighter background color that will not waste ink when printed. We would also like to stay away from wavy banners, or over-the-top graphics that take away from usable space in the deck. Please use a variation of the color scheme in the "Brand Standards" file attached.

```html
<!DOCTYPE html>
<html lang="en">
<head>
<meta charset="utf-8">
<title>Tarrowmead Group – Corporate Presentation Template</title>
<link href="https://fonts.googleapis.com/css2?family=Lato:wght@400;700;900&display=swap" rel="stylesheet">
<style>
:root{
  --red:#9e1b24;
  --red-soft:#c98a8f;
  --dark:#4b4b4d;
  --gray:#6d6d6f;
  --mid:#8a8a8c;
  --light:#ececed;
  --text:#6a6a6a;
  --white:#ffffff;
  --canvas:#ffffff;
}
*{box-sizing:border-box;margin:0;padding:0}
html,body{width:1200px;height:4000px;overflow:hidden;background:var(--canvas)}
body{font-family:"Lato",Arial,sans-serif;color:var(--text)}
.deck{width:1200px;height:4000px;padding:40px;display:grid;grid-template-columns:540px 540px;grid-template-rows:repeat(11,304px);column-gap:40px;align-content:space-between}
.slide{position:relative;width:540px;height:304px;background:var(--white);overflow:hidden;box-shadow:0 1px 5px rgba(0,0,0,.28)}
.abs{position:absolute}
.photo{position:absolute}
.title{font-weight:700;font-size:15px;color:var(--dark);line-height:1.15}
.title b{color:var(--red);font-weight:700}
.title.red{color:var(--red)}
.title.center{text-align:center;left:0;right:0}
.rule{position:absolute;left:50%;transform:translateX(-50%);display:flex;gap:3px}
.rule i{display:block;width:16px;height:2px;background:var(--dark)}
.rule i:nth-child(2){background:var(--red)}
.body{font-size:6px;line-height:1.5;color:var(--text)}
.body.red{color:var(--red);font-weight:700;font-size:7px}
.body.white{color:var(--white)}
.lead{font-weight:700;font-size:10px;line-height:1.3;color:var(--white)}
.bullets{list-style:none;font-size:6px;line-height:1.5;color:var(--text)}
.bullets li{position:relative;padding-left:9px;margin-bottom:4px}
.bullets li::before{content:"";position:absolute;left:0;top:2px;width:4px;height:4px;background:var(--red)}
.bullets b{color:var(--red)}
.mark{display:flex;align-items:center;gap:4px;font-weight:900;letter-spacing:.5px;color:var(--dark);font-size:8px;line-height:1}
.mark::before{content:"";width:10px;height:10px;background:var(--red)}
.mark.light{color:var(--white)}
.mark.light::before{background:var(--white)}
.mark.big{font-size:20px;gap:8px}
.mark.big::before{width:22px;height:22px}
.foot{position:absolute;left:14px;bottom:10px}
.pageno{position:absolute;right:12px;bottom:10px;font-size:5px;color:var(--mid)}
.box{position:absolute;color:var(--white)}
.box h4{font-size:8px;font-weight:700;line-height:1.2}
.box p{font-size:5px;line-height:1.45;margin-top:3px}
.bg-red{background:var(--red)}
.bg-dark{background:var(--dark)}
.bg-gray{background:var(--gray)}
.bg-mid{background:var(--mid)}
.icon{display:block}
.circle{position:absolute;border-radius:50%;display:flex;align-items:center;justify-content:center}
.cap{font-size:7px;font-weight:700;color:var(--dark);text-align:center;line-height:1.2}
.year{font-size:12px;font-weight:700;color:var(--dark)}
</style>
</head>
<body>
<main class="deck">

<!-- 1 Cover -->
<section class="slide">
  <div class="photo" role="img" aria-label="Construction workers pouring concrete at a job site, tinted dark red" style="inset:0;background:linear-gradient(135deg,#5a2a2e,#7d3a3a 45%,#4a3f3c)"></div>
  <div class="abs" style="left:0;right:0;top:64px;display:flex;justify-content:center"><span class="mark big light">TARROWMEAD</span></div>
  <div class="abs" style="left:0;right:0;top:190px;text-align:center;border-top:1px solid rgba(255,255,255,.5);margin:0 150px;padding-top:12px">
    <div class="title" style="color:#fff;font-size:18px">LOREM IPSUM DOLOR</div>
    <div class="body white" style="margin-top:6px">Lorem ipsum dolor sit amet, consectetuer adipiscing elit.<br>Aenean commodo ligula eget dolor.</div>
  </div>
</section>

<!-- 2 Section -->
<section class="slide">
  <div class="photo" role="img" aria-label="Wheelbarrow of fresh concrete being poured" style="left:0;right:0;top:40px;bottom:0;background:linear-gradient(90deg,#6e6e70 0%,#8c8a86 45%,#a7a39c 100%)"></div>
  <div class="title" style="position:absolute;right:16px;top:14px;color:var(--red)">LOREM <span style="font-weight:400">ipsum dolor</span></div>
  <div class="abs bg-dark" style="left:0;top:40px;width:230px;height:70px;opacity:.92;padding:14px 16px">
    <div class="lead" style="font-weight:400;font-size:12px">Aenean massa.<br>Cum sociis natoque.</div>
  </div>
  <div class="abs" style="left:16px;top:150px"><span class="mark big light">TARROWMEAD</span></div>
</section>

<!-- 3 Text with panel left -->
<section class="slide">
  <div class="abs bg-gray" style="left:0;top:0;width:200px;height:260px;padding:60px 22px 0">
    <div class="circle" style="position:static;width:34px;height:34px;border:1.5px solid #fff;margin:0 auto 14px">
      <svg class="icon" width="18" height="18" viewBox="0 0 24 24" fill="none" stroke="#fff" stroke-width="1.6"><circle cx="12" cy="12" r="9"/><path d="M3 12h18M12 3c3 3 3 15 0 18M12 3c-3 3-3 15 0 18"/></svg>
    </div>
    <div class="lead" style="text-align:center">Lorem ipsum dolor sit amet, consectetuer adipiscing elit. Aenean commodo ligula eget dolor.</div>
  </div>
  <div class="abs" style="left:216px;top:16px;right:18px">
    <div class="title">LOREM <b>ipsum dolor sit amet</b></div>
    <div class="body red" style="margin-top:6px">Lorem ipsum dolor sit amet, consectetuer adipiscing elit. Aenean commodo ligula eget dolor.</div>
    <p class="body" style="margin-top:6px">Lorem ipsum dolor sit amet, consectetuer adipiscing elit. Aenean commodo ligula eget dolor. Aenean massa. Cum sociis natoque penatibus et magnis dis parturient montes, nascetur ridiculus mus. Donec quam felis, ultricies nec, pellentesque eu.</p>
    <ul class="bullets" style="margin-top:6px">
      <li>Lorem ipsum dolor sit amet, consectetuer adipiscing elit aenean commodo.</li>
      <li>Cum sociis natoque penatibus et magnis dis parturient montes nascetur.</li>
      <li>Donec quam felis, ultricies nec, pellentesque eu, pretium quis sem.</li>
    </ul>
    <p class="body" style="margin-top:4px">Nulla consequat massa quis enim. Donec pede justo, fringilla vel, aliquet nec, vulputate eget, arcu. In enim justo, rhoncus ut imperdiet.</p>
  </div>
  <div class="foot"><span class="mark">TARROWMEAD</span></div>
  <span class="pageno">3</span>
</section>

<!-- 4 Text with panel right -->
<section class="slide">
  <div class="abs" style="left:18px;top:16px;width:300px">
    <div class="title red">Lorem ipsum dolor sit amet</div>
    <div class="body red" style="margin-top:6px">Lorem ipsum dolor sit amet, consectetuer adipiscing elit. Aenean commodo ligula eget dolor.</div>
    <p class="body" style="margin-top:6px">Lorem ipsum dolor sit amet, consectetuer adipiscing elit. Aenean commodo ligula eget dolor. Aenean massa. Cum sociis natoque penatibus et magnis dis parturient montes, nascetur ridiculus mus. Donec quam felis, ultricies nec.</p>
    <ul class="bullets" style="margin-top:6px">
      <li>Lorem ipsum dolor sit amet, consectetuer adipiscing elit aenean commodo.</li>
      <li>Cum sociis natoque penatibus et magnis dis parturient montes nascetur.</li>
      <li>Donec quam felis, ultricies nec, pellentesque eu, pretium quis sem.</li>
    </ul>
    <p class="body" style="margin-top:4px">Nulla consequat massa quis enim. Donec pede justo, fringilla vel, aliquet nec, vulputate eget, arcu. In enim justo, rhoncus ut.</p>
  </div>
  <div class="abs bg-red" style="right:0;top:0;width:190px;height:304px;padding:80px 22px 0">
    <div class="circle" style="position:static;width:34px;height:34px;border:1.5px solid #fff;margin:0 auto 14px">
      <svg class="icon" width="18" height="18" viewBox="0 0 24 24" fill="none" stroke="#fff" stroke-width="1.6"><circle cx="12" cy="12" r="9"/><path d="M3 12h18M12 3c3 3 3 15 0 18M12 3c-3 3-3 15 0 18"/></svg>
    </div>
    <div class="lead" style="text-align:center">Lorem ipsum dolor sit amet, consectetuer adipiscing elit. Aenean commodo ligula eget dolor.</div>
  </div>
  <div class="foot"><span class="mark">TARROWMEAD</span></div>
</section>

<!-- 5 Panel, photo, text -->
<section class="slide">
  <div class="abs bg-red" style="left:0;top:0;width:160px;height:304px;padding:70px 18px 0">
    <svg class="icon" width="30" height="30" viewBox="0 0 24 24" fill="#fff" style="margin:0 auto 16px"><path d="M21 16v-2l-8-5V3.5a1.5 1.5 0 0 0-3 0V9l-8 5v2l8-2.5V19l-2 1.5V22l3.5-1 3.5 1v-1.5L13 19v-5.5z"/></svg>
    <div class="lead" style="text-align:center">Lorem ipsum dolor sit amet, consectetuer adipiscing elit. Aenean commodo ligula eget dolor.</div>
  </div>
  <div class="photo" role="img" aria-label="Engineer working at industrial equipment in blue light" style="left:160px;top:0;width:170px;height:304px;background:linear-gradient(160deg,#2d4c6e,#5b7c9a 50%,#8a6b5a)"></div>
  <div class="abs" style="left:342px;top:16px;right:14px">
    <div class="title">LOREM <b>ipsum</b></div>
    <div class="body red" style="margin-top:4px">Lorem ipsum dolor sit amet, consectetuer adipiscing elit.</div>
    <ul class="bullets" style="margin-top:8px">
      <li>Lorem ipsum dolor sit amet consectetuer.</li>
      <li>Aenean commodo ligula eget dolor.</li>
      <li>Aenean massa cum sociis.</li>
      <li>Donec quam felis, ultricies nec pellentesque eu pretium.</li>
      <li>Nulla consequat massa quis enim donec pede justo.</li>
      <li>Fringilla vel aliquet nec vulputate eget arcu.</li>
    </ul>
    <p class="body" style="margin-top:6px">In enim justo, rhoncus ut, imperdiet a, venenatis vitae, justo. Nullam dictum felis eu pede mollis pretium.</p>
  </div>
  <span class="pageno">5</span>
</section>

<!-- 6 Three boxes with photo strip -->
<section class="slide">
  <div class="title center abs" style="top:14px">LOREM <b>ipsum dolor sit amet</b></div>
  <div class="rule" style="top:34px"><i></i><i></i><i></i></div>
  <p class="body abs" style="top:42px;left:30px;right:30px;text-align:center">Lorem ipsum dolor sit amet, consectetuer adipiscing elit. Aenean commodo ligula eget dolor. Aenean massa. Cum sociis natoque penatibus et magnis dis parturient montes, nascetur ridiculus mus. Donec quam felis, ultricies nec.</p>
  <div class="box bg-dark" style="left:50px;top:80px;width:120px;height:38px;padding:8px;text-align:center"><h4>Lorem ipsum<br>dolor sit amet</h4></div>
  <div class="box bg-dark" style="left:210px;top:80px;width:120px;height:38px;padding:8px;text-align:center"><h4>Lorem ipsum<br>dolor sit amet</h4></div>
  <div class="box bg-dark" style="left:370px;top:80px;width:120px;height:38px;padding:8px;text-align:center"><h4>Lorem ipsum<br>dolor sit amet</h4></div>
  <div class="abs" style="left:50px;top:120px;width:440px;display:flex;justify-content:space-between">
    <p class="body" style="width:120px;text-align:center">Lorem ipsum dolor sit amet, consectetuer adipiscing elit aenean.</p>
    <p class="body" style="width:120px;text-align:center">Lorem ipsum dolor sit amet, consectetuer adipiscing elit aenean.</p>
    <p class="body" style="width:120px;text-align:center">Lorem ipsum dolor sit amet, consectetuer adipiscing elit aenean.</p>
  </div>
  <div class="photo" role="img" aria-label="City street with ornate stone buildings" style="left:0;right:0;top:170px;height:110px;background:linear-gradient(90deg,#8c7a5e,#c9b48d 40%,#a89272 70%,#7d6a52)"></div>
  <div class="foot" style="bottom:6px"><span class="mark">TARROWMEAD</span></div>
</section>

<!-- 7 Full photo with statement -->
<section class="slide">
  <div class="photo" role="img" aria-label="Climbers helping each other up a rock at sunset, tinted red" style="inset:0;background:linear-gradient(120deg,#5b2440,#8d2f3a 50%,#b85a45)"></div>
  <div class="lead abs" style="right:20px;top:100px;width:220px;font-size:11px">Lorem ipsum dolor sit amet, consectetuer adipiscing elit. Aenean commodo ligula eget dolor.</div>
</section>

<!-- 8 Three icons -->
<section class="slide">
  <div class="title center abs" style="top:14px">LOREM <b>ipsum dolor sit amet</b></div>
  <div class="rule" style="top:34px"><i></i><i></i><i></i></div>
  <p class="body abs" style="top:42px;left:30px;right:30px;text-align:center">Lorem ipsum dolor sit amet, consectetuer adipiscing elit. Aenean commodo ligula eget dolor. Aenean massa. Cum sociis natoque penatibus et magnis dis parturient montes, nascetur ridiculus mus. Donec quam felis.</p>
  <div class="circle bg-dark" style="left:92px;top:110px;width:40px;height:40px"><svg width="20" height="20" viewBox="0 0 24 24" fill="#fff"><rect x="3" y="12" width="4" height="8"/><rect x="10" y="7" width="4" height="13"/><rect x="17" y="4" width="4" height="16"/></svg></div>
  <div class="circle bg-red" style="left:250px;top:104px;width:48px;height:48px"><svg width="22" height="22" viewBox="0 0 24 24" fill="#fff"><path d="M12 2l8 3v6c0 5-3.5 9-8 11-4.5-2-8-6-8-11V5z"/></svg></div>
  <div class="circle bg-dark" style="left:408px;top:110px;width:40px;height:40px"><svg width="20" height="20" viewBox="0 0 24 24" fill="none" stroke="#fff" stroke-width="2"><circle cx="9" cy="10" r="4"/><circle cx="17" cy="16" r="3"/></svg></div>
  <div class="cap abs" style="left:62px;top:160px;width:100px">Lorem ipsum<br>dolor sit amet</div>
  <div class="cap abs" style="left:224px;top:160px;width:100px">Lorem ipsum<br>dolor sit amet</div>
  <div class="cap abs" style="left:378px;top:160px;width:100px">Lorem ipsum<br>dolor sit amet</div>
  <div class="abs bg-red" style="left:0;right:0;top:200px;height:54px;padding:12px 40px"><p class="body white" style="text-align:center">Lorem ipsum dolor sit amet, consectetuer adipiscing elit. Aenean commodo ligula eget dolor. Aenean massa. Cum sociis natoque penatibus et magnis dis parturient montes, nascetur ridiculus mus. Donec quam felis, ultricies nec, pellentesque eu, pretium quis, sem.</p></div>
  <div class="foot"><span class="mark">TARROWMEAD</span></div>
</section>

<!-- 9 Six tiles -->
<section class="slide">
  <div class="title abs" style="left:18px;top:14px">LOREM <b>ipsum dolor sit amet</b></div>
  <p class="body abs" style="left:18px;right:18px;top:34px">Lorem ipsum dolor sit amet, consectetuer adipiscing elit. Aenean commodo ligula eget dolor. Aenean massa. Cum sociis natoque penatibus et magnis dis parturient montes, nascetur ridiculus mus.</p>
  <div class="box bg-dark" style="left:18px;top:66px;width:164px;height:80px;padding:10px"><h4>■ Lorem ipsum dolor</h4><p>Lorem ipsum dolor sit amet, consectetuer adipiscing elit. Aenean commodo ligula eget dolor massa.</p></div>
  <div class="box bg-red" style="left:188px;top:66px;width:164px;height:80px;padding:10px"><h4>■ Lorem ipsum dolor</h4><p>Lorem ipsum dolor sit amet, consectetuer adipiscing elit. Aenean commodo ligula eget dolor massa.</p></div>
  <div class="box bg-dark" style="left:358px;top:66px;width:164px;height:80px;padding:10px"><h4>■ Lorem ipsum dolor</h4><p>Lorem ipsum dolor sit amet, consectetuer adipiscing elit. Aenean commodo ligula eget dolor massa.</p></div>
  <div class="box bg-dark" style="left:18px;top:152px;width:164px;height:80px;padding:10px"><h4>■ Lorem ipsum dolor</h4><p>Lorem ipsum dolor sit amet, consectetuer adipiscing elit. Aenean commodo ligula eget dolor massa.</p></div>
  <div class="box bg-red" style="left:188px;top:152px;width:164px;height:80px;padding:10px"><h4>■ Lorem ipsum dolor</h4><p>Lorem ipsum dolor sit amet, consectetuer adipiscing elit. Aenean commodo ligula eget dolor massa.</p></div>
  <div class="box bg-dark" style="left:358px;top:152px;width:164px;height:80px;padding:10px"><h4>■ Lorem ipsum dolor</h4><p>Lorem ipsum dolor sit amet, consectetuer adipiscing elit. Aenean commodo ligula eget dolor massa.</p></div>
  <div class="foot"><span class="mark">TARROWMEAD</span></div>
  <span class="pageno">9</span>
</section>

<!-- 10 Text with photo grid -->
<section class="slide">
  <div class="title abs" style="left:18px;top:14px">LOREM <b>ipsum dolor sit amet</b></div>
  <div class="abs" style="left:18px;top:40px;width:230px">
    <p class="body">Lorem ipsum dolor sit amet, consectetuer adipiscing elit. Aenean commodo ligula eget dolor. Aenean massa. Cum sociis natoque penatibus et magnis dis parturient montes, nascetur ridiculus mus. Donec quam felis, ultricies nec, pellentesque eu, pretium quis, sem.</p>
    <p class="body" style="margin-top:6px">Nulla consequat massa quis enim. Donec pede justo, fringilla vel, aliquet nec, vulputate eget, arcu. In enim justo, rhoncus ut, imperdiet a, venenatis vitae, justo. Nullam dictum felis eu pede mollis pretium.</p>
    <p class="body" style="margin-top:6px">Integer tincidunt. Cras dapibus. Vivamus elementum semper nisi. Aenean vulputate eleifend tellus. Aenean leo ligula, porttitor eu, consequat vitae, eleifend ac, enim.</p>
  </div>
  <div class="photo" role="img" aria-label="Industrial machinery close-up" style="left:262px;top:40px;width:84px;height:70px;background:linear-gradient(135deg,#5a5e66,#9aa0a6)"></div>
  <div class="box bg-dark" style="left:350px;top:40px;width:84px;height:70px;padding:8px"><h4>Lorem ipsum dolor sit</h4><p>Lorem ipsum dolor sit amet elit.</p></div>
  <div class="photo" role="img" aria-label="Steel pipes at a plant" style="left:438px;top:40px;width:84px;height:70px;background:linear-gradient(135deg,#6b6f75,#b3b6ba)"></div>
  <div class="photo" role="img" aria-label="Worker with hard hat on site" style="left:262px;top:114px;width:84px;height:70px;background:linear-gradient(135deg,#3c3f45,#7d7466)"></div>
  <div class="photo" role="img" aria-label="Electrical panel wiring" style="left:350px;top:114px;width:84px;height:70px;background:linear-gradient(135deg,#2e3a4c,#56657a)"></div>
  <div class="photo" role="img" aria-label="Gears and mechanical parts" style="left:438px;top:114px;width:84px;height:70px;background:linear-gradient(135deg,#5e5448,#a28c6c)"></div>
  <div class="photo" role="img" aria-label="Welder sparks in workshop" style="left:262px;top:188px;width:84px;height:70px;background:linear-gradient(135deg,#3a2a24,#c06a3a)"></div>
  <div class="photo" role="img" aria-label="Construction tools on a table" style="left:350px;top:188px;width:84px;height:70px;background:linear-gradient(135deg,#4c4c4e,#8e8c88)"></div>
  <div class="photo" role="img" aria-label="Technician checking gauges" style="left:438px;top:188px;width:84px;height:70px;background:linear-gradient(135deg,#4a3c34,#8a6e5a)"></div>
  <div class="foot"><span class="mark">TARROWMEAD</span></div>
</section>

<!-- 11 Mixed tile grid -->
<section class="slide">
  <div class="title red center abs" style="top:14px">Lorem ipsum dolor sit amet</div>
  <div class="rule" style="top:34px"><i></i><i></i><i></i></div>
  <div class="photo" role="img" aria-label="Factory machinery" style="left:18px;top:46px;width:124px;height:70px;background:linear-gradient(135deg,#4e5258,#8f949a)"></div>
  <div class="box bg-red" style="left:146px;top:46px;width:124px;height:70px;padding:8px"><h4>Lorem ipsum dolor sit</h4><p>Lorem ipsum dolor sit amet consectetuer elit.</p></div>
  <div class="photo" role="img" aria-label="Engine parts in a workshop" style="left:274px;top:46px;width:124px;height:70px;background:linear-gradient(135deg,#5a4a3e,#a48a6c)"></div>
  <div class="box bg-red" style="left:402px;top:46px;width:120px;height:70px;padding:8px"><h4>Lorem ipsum dolor sit</h4><p>Lorem ipsum dolor sit amet consectetuer elit.</p></div>
  <div class="box bg-dark" style="left:18px;top:120px;width:124px;height:70px;padding:8px"><h4>Lorem ipsum dolor sit</h4><p>Lorem ipsum dolor sit amet consectetuer elit.</p></div>
  <div class="photo" role="img" aria-label="Engineers reviewing plans" style="left:146px;top:120px;width:124px;height:70px;background:linear-gradient(135deg,#5c6a7c,#a6b0bc)"></div>
  <div class="box bg-dark" style="left:274px;top:120px;width:124px;height:70px;padding:8px"><h4>Lorem ipsum dolor sit</h4><p>Lorem ipsum dolor sit amet consectetuer elit.</p></div>
  <div class="photo" role="img" aria-label="Tablet with charts on a desk" style="left:402px;top:120px;width:120px;height:70px;background:linear-gradient(135deg,#6c7078,#b8bcc2)"></div>
  <div class="abs" style="left:18px;top:196px;width:504px;display:flex;gap:4px">
    <div style="width:124px"><div class="cap" style="text-align:left">Lorem ipsum dolor</div><p class="body">Lorem ipsum dolor sit amet, consectetuer adipiscing elit.</p></div>
    <div style="width:124px"><div class="cap" style="text-align:left">Lorem ipsum dolor</div><p class="body">Lorem ipsum dolor sit amet, consectetuer adipiscing elit.</p></div>
    <div style="width:124px"><div class="cap" style="text-align:left">Lorem ipsum dolor</div><p class="body">Lorem ipsum dolor sit amet, consectetuer adipiscing elit.</p></div>
    <div style="width:120px"><div class="cap" style="text-align:left">Lorem ipsum dolor</div><p class="body">Lorem ipsum dolor sit amet, consectetuer adipiscing elit.</p></div>
  </div>
  <div class="foot"><span class="mark">TARROWMEAD</span></div>
</section>

<!-- 12 Photo with red column -->
<section class="slide">
  <div class="photo" role="img" aria-label="Sunlit city street with historic buildings" style="inset:0;background:linear-gradient(100deg,#8a7554,#c8b088 40%,#9fa87a 70%,#6e7a54)"></div>
  <div class="abs bg-red" style="left:0;top:0;width:170px;height:304px;opacity:.94;padding:80px 18px 0">
    <svg class="icon" width="34" height="34" viewBox="0 0 40 40" style="margin:0 auto 12px"><circle cx="20" cy="20" r="19" fill="none" stroke="#fff" stroke-width="1.4"/><path d="M11 18a13 13 0 0 1 18 0M14 21a8 8 0 0 1 12 0M17 24a3.5 3.5 0 0 1 6 0" fill="none" stroke="#fff" stroke-width="1.8"/><circle cx="20" cy="27.5" r="1.6" fill="#fff"/></svg>
    <div class="lead" style="text-align:center">Lorem ipsum dolor sit amet, consectetuer adipiscing elit. Aenean commodo ligula eget dolor.</div>
  </div>
</section>

<!-- 13 Four boxes with central icon -->
<section class="slide">
  <div class="title center abs" style="top:14px">LOREM <b>ipsum dolor sit amet</b></div>
  <div class="rule" style="top:34px"><i></i><i></i><i></i></div>
  <p class="body abs" style="top:42px;left:30px;right:30px;text-align:center">Lorem ipsum dolor sit amet, consectetuer adipiscing elit. Aenean commodo ligula eget dolor. Aenean massa. Cum sociis natoque penatibus et magnis dis parturient montes, nascetur ridiculus mus.</p>
  <div class="box bg-dark" style="left:24px;top:76px;width:118px;height:96px;padding:10px"><h4 style="text-align:center">Lorem ipsum<br>dolor sit amet</h4><p>Lorem ipsum dolor sit amet, consectetuer adipiscing elit aenean commodo.</p></div>
  <div class="box bg-dark" style="left:150px;top:76px;width:118px;height:96px;padding:10px"><h4 style="text-align:center">Lorem ipsum<br>dolor sit amet</h4><p>Lorem ipsum dolor sit amet, consectetuer adipiscing elit aenean commodo.</p></div>
  <div class="box bg-dark" style="left:276px;top:76px;width:118px;height:96px;padding:10px"><h4 style="text-align:center">Lorem ipsum<br>dolor sit amet</h4><p>Lorem ipsum dolor sit amet, consectetuer adipiscing elit aenean commodo.</p></div>
  <div class="box bg-dark" style="left:402px;top:76px;width:118px;height:96px;padding:10px"><h4 style="text-align:center">Lorem ipsum<br>dolor sit amet</h4><p>Lorem ipsum dolor sit amet, consectetuer adipiscing elit aenean commodo.</p></div>
  <div class="abs" style="left:24px;right:24px;top:184px;height:1px;background:#cfcfd0"></div>
  <div class="circle bg-red" style="left:245px;top:158px;width:50px;height:50px;border:3px solid #fff"><svg width="24" height="24" viewBox="0 0 24 24" fill="none" stroke="#fff" stroke-width="1.6"><circle cx="12" cy="12" r="9"/><path d="M7 13l3 3 7-7"/></svg></div>
  <p class="body abs" style="left:40px;top:214px;width:180px">Lorem ipsum dolor sit amet, consectetuer adipiscing elit. Aenean commodo ligula eget dolor. Aenean massa cum sociis.</p>
  <p class="body abs" style="left:320px;top:214px;width:180px">Lorem ipsum dolor sit amet, consectetuer adipiscing elit. Aenean commodo ligula eget dolor. Aenean massa cum sociis.</p>
  <div class="foot"><span class="mark">TARROWMEAD</span></div>
</section>

<!-- 14 Profile -->
<section class="slide">
  <div class="abs" style="left:18px;top:16px;width:320px">
    <div class="title">LOREM <b>ipsum dolor sit amet</b></div>
    <div class="body red" style="margin-top:4px">Lorem ipsum dolor sit amet, consectetuer adipiscing elit. Aenean commodo ligula eget dolor.</div>
    <ul class="bullets" style="margin-top:12px">
      <li><b>Lorem ipsum dolor sit amet</b>, consectetuer adipiscing elit. Aenean commodo ligula eget dolor aenean massa cum sociis.</li>
      <li><b>Lorem ipsum dolor sit amet</b>, consectetuer adipiscing elit. Aenean commodo ligula eget dolor aenean massa cum sociis.</li>
      <li><b>Lorem ipsum dolor sit amet</b>, consectetuer adipiscing elit. Aenean commodo ligula eget dolor aenean massa cum sociis.</li>
      <li><b>Lorem ipsum dolor sit amet</b>, consectetuer adipiscing elit. Aenean commodo ligula eget dolor aenean massa cum sociis.</li>
    </ul>
  </div>
  <div class="photo" role="img" aria-label="Portrait of a smiling businessman in a suit" style="left:350px;top:20px;width:170px;height:220px;background:radial-gradient(ellipse at 50% 30%,#d9d6d2,#5a5a5e 70%,#2f2f33)"></div>
  <div class="abs bg-red" style="left:0;right:0;top:240px;height:22px;padding:6px 18px"><span class="body white" style="font-weight:700">Lorem ipsum dolor sit amet, consectetuer adipiscing elit.</span></div>
  <div class="foot"><span class="mark">TARROWMEAD</span></div>
</section>

<!-- 15 Five columns -->
<section class="slide">
  <div class="title center abs" style="top:14px">LOREM <b>ipsum dolor sit amet</b></div>
  <div class="body red abs" style="top:34px;left:20px;right:20px;text-align:center;font-size:6.5px">Lorem ipsum dolor sit amet, consectetuer adipiscing elit. Aenean commodo ligula eget dolor. Aenean massa. Cum sociis natoque penatibus et magnis dis parturient montes.</div>
  <p class="body abs" style="top:50px;left:20px;right:20px;text-align:center">Lorem ipsum dolor sit amet, consectetuer adipiscing elit. Aenean commodo ligula eget dolor. Aenean massa. Cum sociis natoque penatibus et magnis dis parturient montes, nascetur ridiculus mus. Donec quam felis, ultricies nec, pellentesque eu.</p>
  <div class="box bg-red" style="left:0;top:84px;width:108px;height:150px;padding:18px 10px;text-align:center"><svg width="22" height="22" viewBox="0 0 24 24" fill="#fff"><rect x="3" y="12" width="4" height="8"/><rect x="10" y="7" width="4" height="13"/><rect x="17" y="4" width="4" height="16"/></svg><h4 style="margin-top:8px">Lorem ipsum dolor</h4><p>Lorem ipsum dolor sit amet, consectetuer adipiscing elit aenean commodo ligula.</p></div>
  <div class="box" style="left:108px;top:84px;width:108px;height:150px;padding:18px 10px;text-align:center;background:#b5353c"><svg width="22" height="22" viewBox="0 0 24 24" fill="#fff"><path d="M12 2l8 3v6c0 5-3.5 9-8 11-4.5-2-8-6-8-11V5z"/></svg><h4 style="margin-top:8px">Lorem ipsum dolor</h4><p>Lorem ipsum dolor sit amet, consectetuer adipiscing elit aenean commodo ligula.</p></div>
  <div class="box bg-dark" style="left:216px;top:84px;width:108px;height:150px;padding:18px 10px;text-align:center"><svg width="22" height="22" viewBox="0 0 24 24" fill="none" stroke="#fff" stroke-width="2"><circle cx="9" cy="10" r="4"/><circle cx="17" cy="16" r="3"/></svg><h4 style="margin-top:8px">Lorem ipsum dolor</h4><p>Lorem ipsum dolor sit amet, consectetuer adipiscing elit aenean commodo ligula.</p></div>
  <div class="box bg-mid" style="left:324px;top:84px;width:108px;height:150px;padding:18px 10px;text-align:center"><svg width="22" height="22" viewBox="0 0 24 24" fill="#fff"><path d="M2 20V10l5 3V10l5 3V6h4v14z"/></svg><h4 style="margin-top:8px">Lorem ipsum dolor</h4><p>Lorem ipsum dolor sit amet, consectetuer adipiscing elit aenean commodo ligula.</p></div>
  <div class="box bg-gray" style="left:432px;top:84px;width:108px;height:150px;padding:18px 10px;text-align:center"><svg width="22" height="22" viewBox="0 0 24 24" fill="none" stroke="#fff" stroke-width="2"><rect x="4" y="4" width="16" height="16" rx="2"/><path d="M4 9h16M9 4v16"/></svg><h4 style="margin-top:8px">Lorem ipsum dolor</h4><p>Lorem ipsum dolor sit amet, consectetuer adipiscing elit aenean commodo ligula.</p></div>
  <div class="foot"><span class="mark">TARROWMEAD</span></div>
</section>

<!-- 16 Team -->
<section class="slide">
  <div class="title center abs" style="top:14px">LOREM <b>ipsum dolor sit amet</b></div>
  <div class="rule" style="top:34px"><i></i><i></i><i></i></div>
  <div class="abs" style="left:30px;right:30px;top:52px;display:flex;justify-content:space-between">
    <div style="width:100px;text-align:center">
      <div class="photo" role="img" aria-label="Team member portrait" style="position:relative;width:58px;height:58px;margin:0 auto;border-radius:50%;background:radial-gradient(circle at 50% 40%,#c9c5c0,#55555a);border:2px solid var(--red)"></div>
      <div class="cap" style="margin-top:8px;font-size:8px">Lorem Ipsum</div><div style="font-size:5px;color:var(--red)">LOREM IPSUM DOLOR</div>
      <p class="body" style="margin-top:4px">Lorem ipsum dolor sit amet, consectetuer adipiscing elit aenean commodo.</p>
      <div style="display:flex;gap:3px;justify-content:center;margin-top:5px"><i style="width:9px;height:9px;border-radius:50%;background:var(--red)"></i><i style="width:9px;height:9px;border-radius:50%;background:var(--dark)"></i><i style="width:9px;height:9px;border-radius:50%;background:var(--gray)"></i></div>
    </div>
    <div style="width:100px;text-align:center">
      <div class="photo" role="img" aria-label="Team member portrait" style="position:relative;width:58px;height:58px;margin:0 auto;border-radius:50%;background:radial-gradient(circle at 50% 40%,#c9c5c0,#55555a);border:2px solid var(--red)"></div>
      <div class="cap" style="margin-top:8px;font-size:8px">Lorem Ipsum</div><div style="font-size:5px;color:var(--red)">LOREM IPSUM DOLOR</div>
      <p class="body" style="margin-top:4px">Lorem ipsum dolor sit amet, consectetuer adipiscing elit aenean commodo.</p>
      <div style="display:flex;gap:3px;justify-content:center;margin-top:5px"><i style="width:9px;height:9px;border-radius:50%;background:var(--red)"></i><i style="width:9px;height:9px;border-radius:50%;background:var(--dark)"></i><i style="width:9px;height:9px;border-radius:50%;background:var(--gray)"></i></div>
    </div>
    <div style="width:100px;text-align:center">
      <div class="photo" role="img" aria-label="Team member portrait" style="position:relative;width:58px;height:58px;margin:0 auto;border-radius:50%;background:radial-gradient(circle at 50% 40%,#c9c5c0,#55555a);border:2px solid var(--red)"></div>
      <div class="cap" style="margin-top:8px;font-size:8px">Lorem Ipsum</div><div style="font-size:5px;color:var(--red)">LOREM IPSUM DOLOR</div>
      <p class="body" style="margin-top:4px">Lorem ipsum dolor sit amet, consectetuer adipiscing elit aenean commodo.</p>
      <div style="display:flex;gap:3px;justify-content:center;margin-top:5px"><i style="width:9px;height:9px;border-radius:50%;background:var(--red)"></i><i style="width:9px;height:9px;border-radius:50%;background:var(--dark)"></i><i style="width:9px;height:9px;border-radius:50%;background:var(--gray)"></i></div>
    </div>
    <div style="width:100px;text-align:center">
      <div class="photo" role="img" aria-label="Team member portrait" style="position:relative;width:58px;height:58px;margin:0 auto;border-radius:50%;background:radial-gradient(circle at 50% 40%,#c9c5c0,#55555a);border:2px solid var(--red)"></div>
      <div class="cap" style="margin-top:8px;font-size:8px">Lorem Ipsum</div><div style="font-size:5px;color:var(--red)">LOREM IPSUM DOLOR</div>
      <p class="body" style="margin-top:4px">Lorem ipsum dolor sit amet, consectetuer adipiscing elit aenean commodo.</p>
      <div style="display:flex;gap:3px;justify-content:center;margin-top:5px"><i style="width:9px;height:9px;border-radius:50%;background:var(--red)"></i><i style="width:9px;height:9px;border-radius:50%;background:var(--dark)"></i><i style="width:9px;height:9px;border-radius:50%;background:var(--gray)"></i></div>
    </div>
  </div>
  <span class="pageno">16</span>
</section>

<!-- 17 Timeline -->
<section class="slide">
  <div class="title red center abs" style="top:14px">Lorem ipsum dolor sit amet</div>
  <p class="body abs" style="top:34px;left:30px;right:30px;text-align:center">Lorem ipsum dolor sit amet, consectetuer adipiscing elit. Aenean commodo ligula eget dolor. Aenean massa. Cum sociis natoque penatibus et magnis dis parturient montes.</p>
  <div class="rule" style="top:56px"><i></i><i></i><i></i></div>
  <span class="year abs" style="left:30px;top:84px">2012</span>
  <span class="year abs" style="left:190px;top:84px">2014</span>
  <span class="year abs" style="left:350px;top:84px">2016</span>
  <p class="body abs" style="left:84px;top:98px;width:100px;border-left:1px solid #bbb;padding-left:4px">Lorem ipsum dolor sit amet consectetuer adipiscing elit.</p>
  <p class="body abs" style="left:244px;top:98px;width:100px;border-left:1px solid #bbb;padding-left:4px">Lorem ipsum dolor sit amet consectetuer adipiscing elit.</p>
  <p class="body abs" style="left:404px;top:98px;width:100px;border-left:1px solid #bbb;padding-left:4px">Lorem ipsum dolor sit amet consectetuer adipiscing elit.</p>
  <svg class="abs" style="left:24px;top:136px" width="492" height="26" viewBox="0 0 492 26">
    <polygon points="0,0 76,0 86,13 76,26 0,26" fill="#7d1219"/>
    <polygon points="80,0 156,0 166,13 156,26 80,26 90,13" fill="#9e1b24"/>
    <polygon points="160,0 236,0 246,13 236,26 160,26 170,13" fill="#b94a52"/>
    <polygon points="240,0 316,0 326,13 316,26 240,26 250,13" fill="#d08088"/>
    <polygon points="320,0 396,0 406,13 396,26 320,26 330,13" fill="#e2aeb2"/>
    <polygon points="400,0 482,0 492,13 482,26 400,26 410,13" fill="#efd0d2"/>
  </svg>
  <p class="body abs" style="left:84px;top:170px;width:100px;border-left:1px solid #bbb;padding-left:4px">Lorem ipsum dolor sit amet consectetuer adipiscing elit.</p>
  <p class="body abs" style="left:244px;top:170px;width:100px;border-left:1px solid #bbb;padding-left:4px">Lorem ipsum dolor sit amet consectetuer adipiscing elit.</p>
  <p class="body abs" style="left:404px;top:170px;width:100px;border-left:1px solid #bbb;padding-left:4px">Lorem ipsum dolor sit amet consectetuer adipiscing elit.</p>
  <span class="year abs" style="left:110px;top:206px">2013</span>
  <span class="year abs" style="left:270px;top:206px">2015</span>
  <span class="year abs" style="left:470px;top:206px">2017</span>
  <div class="foot"><span class="mark">TARROWMEAD</span></div>
</section>

<!-- 18 Process chevrons -->
<section class="slide">
  <div class="title red center abs" style="top:14px">Lorem ipsum dolor sit amet</div>
  <p class="body abs" style="top:34px;left:30px;right:30px;text-align:center">Lorem ipsum dolor sit amet, consectetuer adipiscing elit. Aenean commodo ligula eget dolor. Aenean massa. Cum sociis natoque penatibus et magnis dis parturient montes.</p>
  <div class="rule" style="top:56px"><i></i><i></i><i></i></div>
  <svg class="abs" style="left:18px;top:78px" width="504" height="110" viewBox="0 0 504 110">
    <polygon points="0,0 150,0 176,55 150,110 0,110 18,55" fill="#9e1b24"/>
    <polygon points="164,0 318,0 344,55 318,110 164,110 190,55" fill="#4b4b4d"/>
    <polygon points="332,0 478,0 504,55 478,110 332,110 358,55" fill="#6d6d6f"/>
  </svg>
  <div class="box" style="left:44px;top:90px;width:120px"><h4>■ Lorem ipsum dolor</h4><p>Lorem ipsum dolor sit amet, consectetuer adipiscing elit. Aenean commodo ligula eget dolor. Aenean massa cum sociis.</p></div>
  <div class="box" style="left:214px;top:90px;width:120px"><h4>■ Lorem ipsum dolor</h4><p>Lorem ipsum dolor sit amet, consectetuer adipiscing elit. Aenean commodo ligula eget dolor. Aenean massa cum sociis.</p></div>
  <div class="box" style="left:382px;top:90px;width:116px"><h4>■ Lorem ipsum dolor</h4><p>Lorem ipsum dolor sit amet, consectetuer adipiscing elit. Aenean commodo ligula eget dolor. Aenean massa cum sociis.</p></div>
  <div class="foot"><span class="mark">TARROWMEAD</span></div>
</section>

<!-- 19 Cycle -->
<section class="slide">
  <div class="title red center abs" style="top:14px">Lorem ipsum dolor sit amet</div>
  <p class="body abs" style="top:34px;left:30px;right:30px;text-align:center">Lorem ipsum dolor sit amet, consectetuer adipiscing elit. Aenean commodo ligula eget dolor. Aenean massa. Cum sociis natoque penatibus.</p>
  <div class="rule" style="top:56px"><i></i><i></i><i></i></div>
  <svg class="abs" style="left:205px;top:80px" width="130" height="130" viewBox="-65 -65 130 130">
    <g stroke="#fff" stroke-width="3">
      <path d="M0,-62 A62,62 0 0 1 62,0 L32,0 A32,32 0 0 0 0,-32Z" fill="#4b4b4d"/>
      <path d="M62,0 A62,62 0 0 1 0,62 L0,32 A32,32 0 0 0 32,0Z" fill="#6d6d6f"/>
      <path d="M0,62 A62,62 0 0 1 -62,0 L-32,0 A32,32 0 0 0 0,32Z" fill="#9e1b24"/>
      <path d="M-62,0 A62,62 0 0 1 0,-62 L0,-32 A32,32 0 0 0 -32,0Z" fill="#4b4b4d"/>
    </g>
    <g fill="#fff" font-family="Lato,sans-serif" font-weight="700" font-size="10" text-anchor="middle">
      <text x="-30" y="-24">01</text><text x="30" y="-24">02</text><text x="30" y="32">03</text><text x="-30" y="32">04</text>
    </g>
  </svg>
  <div class="abs" style="left:40px;top:92px;width:150px"><div class="cap" style="text-align:left;font-size:9px">01 Lorem ipsum</div><p class="body">Lorem ipsum dolor sit amet, consectetuer adipiscing elit aenean.</p></div>
  <div class="abs" style="left:350px;top:92px;width:150px"><div class="cap" style="text-align:left;font-size:9px">02 Lorem ipsum</div><p class="body">Lorem ipsum dolor sit amet, consectetuer adipiscing elit aenean.</p></div>
  <div class="abs" style="left:40px;top:166px;width:150px"><div class="cap" style="text-align:left;font-size:9px;color:var(--red)">04 Lorem ipsum</div><p class="body">Lorem ipsum dolor sit amet, consectetuer adipiscing elit aenean.</p></div>
  <div class="abs" style="left:350px;top:166px;width:150px"><div class="cap" style="text-align:left;font-size:9px">03 Lorem ipsum</div><p class="body">Lorem ipsum dolor sit amet, consectetuer adipiscing elit aenean.</p></div>
  <div class="foot"><span class="mark">TARROWMEAD</span></div>
</section>

<!-- 20 Bar chart -->
<section class="slide">
  <div class="abs" style="left:18px;top:16px;width:300px">
    <div class="title">LOREM <b>ipsum dolor sit amet</b></div>
    <ul class="bullets" style="margin-top:40px">
      <li><b>Lorem ipsum dolor sit amet</b>, consectetuer adipiscing elit. Aenean commodo ligula eget dolor aenean massa.</li>
      <li><b>Lorem ipsum dolor sit amet</b>, consectetuer adipiscing elit. Aenean commodo ligula eget dolor aenean massa.</li>
      <li><b>Lorem ipsum dolor sit amet</b>, consectetuer adipiscing elit. Aenean commodo ligula eget dolor aenean massa.</li>
      <li><b>Lorem ipsum dolor sit amet</b>, consectetuer adipiscing elit. Aenean commodo ligula eget dolor aenean massa.</li>
    </ul>
  </div>
  <div class="abs bg-red" style="right:0;top:0;width:200px;height:304px"></div>
  <svg class="abs" style="right:14px;top:40px" width="172" height="180" viewBox="0 0 172 180">
    <g fill="#bdbdbf">
      <rect x="4" y="110" width="12" height="60"/><rect x="24" y="90" width="12" height="80"/><rect x="44" y="70" width="12" height="100"/><rect x="64" y="40" width="12" height="130"/><rect x="84" y="60" width="12" height="110"/><rect x="104" y="20" width="12" height="150"/><rect x="124" y="50" width="12" height="120"/><rect x="144" y="30" width="12" height="140"/>
    </g>
    <line x1="0" y1="170" x2="172" y2="170" stroke="#fff" stroke-width="1"/>
    <g fill="#fff" font-size="6" font-family="Lato,sans-serif" text-anchor="middle">
      <text x="10" y="105">24</text><text x="30" y="85">31</text><text x="50" y="65">38</text><text x="70" y="35">52</text><text x="90" y="55">44</text><text x="110" y="15">60</text><text x="130" y="45">48</text><text x="150" y="25">56</text>
      <text x="10" y="178">Item</text><text x="30" y="178">Item</text><text x="50" y="178">Item</text><text x="70" y="178">Item</text><text x="90" y="178">Item</text><text x="110" y="178">Item</text><text x="130" y="178">Item</text><text x="150" y="178">Item</text>
    </g>
  </svg>
  <div class="abs" style="right:14px;top:232px;width:172px;text-align:right"><div class="lead" style="font-size:8px">Lorem ipsum dolor</div><p class="body white">Lorem ipsum dolor sit amet, consectetuer adipiscing.</p></div>
  <div class="foot"><span class="mark">TARROWMEAD</span></div>
</section>

<!-- 21 Line chart -->
<section class="slide">
  <div class="title center abs" style="top:14px">LOREM <b>IPSUM DOLOR SIT AMET</b></div>
  <div class="rule" style="top:34px"><i></i><i></i><i></i></div>
  <div class="abs" style="left:20px;top:50px;width:250px">
    <div class="cap" style="text-align:left">Lorem ipsum dolor</div>
    <p class="body">Lorem ipsum dolor sit amet consectetuer.</p>
    <svg width="250" height="170" viewBox="0 0 250 170" style="margin-top:4px">
      <g stroke="#e2e2e3" stroke-width="1"><line x1="20" y1="20" x2="250" y2="20"/><line x1="20" y1="60" x2="250" y2="60"/><line x1="20" y1="100" x2="250" y2="100"/><line x1="20" y1="140" x2="250" y2="140"/></g>
      <polyline points="24,130 46,96 68,40 90,54 112,66 134,68 156,74 178,82 200,80 222,98 244,90" fill="none" stroke="#4b4b4d" stroke-width="1.4"/>
      <g fill="#fff" stroke="#4b4b4d" stroke-width="1.2"><circle cx="24" cy="130" r="3"/><circle cx="46" cy="96" r="3"/><circle cx="68" cy="40" r="3"/><circle cx="90" cy="54" r="3"/><circle cx="112" cy="66" r="3"/><circle cx="134" cy="68" r="3"/><circle cx="156" cy="74" r="3"/><circle cx="178" cy="82" r="3"/><circle cx="200" cy="80" r="3"/><circle cx="222" cy="98" r="3"/><circle cx="244" cy="90" r="3"/></g>
      <g fill="#888" font-size="6" font-family="Lato,sans-serif"><text x="4" y="22">80</text><text x="4" y="62">60</text><text x="4" y="102">40</text><text x="4" y="142">20</text></g>
      <g fill="#888" font-size="5" font-family="Lato,sans-serif" text-anchor="middle"><text x="24" y="156">Jan</text><text x="46" y="156">Feb</text><text x="68" y="156">Mar</text><text x="90" y="156">Apr</text><text x="112" y="156">May</text><text x="134" y="156">Jun</text><text x="156" y="156">Jul</text><text x="178" y="156">Aug</text><text x="200" y="156">Sep</text><text x="222" y="156">Oct</text><text x="244" y="156">Nov</text></g>
    </svg>
  </div>
  <div class="abs" style="left:296px;top:56px;width:110px">
    <p class="body">Lorem ipsum dolor sit amet, consectetuer adipiscing elit. Aenean commodo ligula eget dolor. Aenean massa. Cum sociis natoque penatibus et magnis dis parturient montes.</p>
    <p class="body" style="margin-top:8px">Lorem ipsum dolor sit amet, consectetuer adipiscing elit. Aenean commodo ligula eget dolor aenean massa.</p>
  </div>
  <div class="abs" style="left:416px;top:56px;width:106px">
    <ul class="bullets"><li>Lorem ipsum dolor sit amet consectetuer adipiscing.</li><li>Aenean commodo ligula eget dolor aenean massa.</li></ul>
    <p class="body" style="margin-top:6px">Lorem ipsum dolor sit amet, consectetuer adipiscing elit. Aenean commodo ligula eget dolor.</p>
    <ul class="bullets" style="margin-top:6px"><li>Lorem ipsum dolor sit amet consectetuer adipiscing.</li><li>Aenean commodo ligula eget dolor aenean massa.</li></ul>
  </div>
  <div class="foot"><span class="mark">TARROWMEAD</span></div>
  <span class="pageno">21</span>
</section>

<!-- 22 Closing -->
<section class="slide">
  <div class="photo" role="img" aria-label="Modern glass office buildings" style="inset:0;background:linear-gradient(135deg,#5d6470,#8a919b 50%,#6a717c)"></div>
  <div class="abs" style="inset:0;background:rgba(75,75,77,.78)"></div>
  <div class="photo" role="img" aria-label="Smiling businessman in a suit" style="right:30px;top:30px;width:150px;height:190px;background:radial-gradient(ellipse at 50% 30%,#b9b6b2,#4e5058 70%,#3c3e44)"></div>
  <div class="abs" style="left:70px;top:60px;width:220px;height:36px;border:1.5px solid #fff;display:flex;align-items:center;justify-content:center"><span class="title" style="color:#fff;font-size:16px;letter-spacing:1px">LOREM IPSUM</span></div>
  <div class="abs bg-dark" style="left:0;right:0;bottom:0;height:82px"></div>
  <div class="abs" style="left:18px;bottom:14px;width:140px">
    <div class="lead" style="font-size:7px">Lorem ipsum dolor</div>
    <p class="body white">Lorem ipsum dolor sit amet<br>Consectetuer adipiscing elit<br>Aenean commodo ligula</p>
    <div class="lead" style="font-size:7px;margin-top:4px">Lorem ipsum dolor</div>
    <p class="body white">Lorem ipsum dolor sit amet</p>
  </div>
  <div class="abs" style="left:210px;bottom:28px"><span class="mark big light" style="font-size:14px">TARROWMEAD</span></div>
  <div class="abs" style="right:18px;bottom:30px;display:flex;gap:6px">
    <i style="width:14px;height:14px;border-radius:50%;background:#fff;display:block"></i>
    <i style="width:14px;height:14px;border-radius:50%;background:#fff;display:block"></i>
    <i style="width:14px;height:14px;border-radius:50%;background:#fff;display:block"></i>
    <i style="width:14px;height:14px;border-radius:50%;background:#fff;display:block"></i>
  </div>
</section>

</main>
</body>
</html>
```